Killer Webpage Design

I currently have a self-hosted webpage through wordpress at www.vantrelmedia.com - the content is complete and I'm happy with this but I need it designed (no coding) to complete my requirements. I'm happy to take designs which are non-Wordpress if there is specific advantage in this.

My full branding logos are attached along with color files. My main aim is consistent branding across all areas (social media, business cards, emails, websites). I have the rest running but am not happy with the available default selections from Wordpress.

I would prefer to use the darker blue version of the logo as I feel this has more standout in online media, however I would appreciate submissions with both variants to help me choose.

With the homepage I will also want to see blog pages and category pages designed but this can come after I have selected a design to go with,

Sites that I like and are related to my business include the following:
http://www.plumora.com/au/accounting-software/
http://www.taskgriddle.com/home.aspx
https://brimtill.com/register
Updates

Apologies for the confusion - to clarify for designers I am looking for design only, no coding.

FYI - i have now uploaded business cards for an idea of the contemporary style of design completed so far.

Target Market(s)

small to medium business. Not systemised but looking for help and support.

Industry/Entity Type

Business

Requirements
Must have
• I'm looking for a minimalist professional page, with the ability to easily add new sections when required. I will also need a CMS to add blog posts on the go, with the same features that it currently has (comments, social logon etc)

```html
<!DOCTYPE html>
<html lang="en">
<head>
<meta charset="utf-8">
<title>Vantrel Media</title>
<link href="https://fonts.googleapis.com/css2?family=Open+Sans:wght@400;600&family=PT+Sans:wght@400;700&display=swap" rel="stylesheet">
<style>
:root{
  --navy:#062a40;
  --card:#0b3c58;
  --teal:#0abac5;
  --teal-dark:#089ea8;
  --teal-text:#12a9b5;
  --orange:#e8793a;
  --grey:#7a7a7a;
  --line:#d6d6d6;
  --white:#ffffff;
}
*{margin:0;padding:0;box-sizing:border-box}
html,body{width:934px;height:1200px;overflow:hidden;background:var(--white)}
body{position:relative;font-family:"PT Sans",sans-serif;color:var(--grey)}
.abs{position:absolute}

.site-header{left:0;top:0;width:934px;height:82px;background:var(--navy)}
.brand{left:146px;top:26px;display:flex;align-items:center;gap:8px}
.brand-dot{width:26px;height:26px;border-radius:50%;background:var(--teal)}
.brand-name{font-family:"PT Sans",sans-serif;font-weight:700;font-size:22px;color:var(--white)}
.social{left:543px;top:32px;display:flex;gap:7px}
.social span{width:20px;height:20px;border-radius:50%;background:#0d3d5a}
.search{left:635px;top:32px;width:152px;height:21px;background:#0d3d5a;border-radius:2px;color:#dfe8ee;font-size:11px;padding:3px 0 0 15px}
.search svg{position:absolute;right:8px;top:4px}

.main-nav{left:0;top:82px;width:934px;height:31px;display:flex;justify-content:center;align-items:center;font-size:9.5px;text-transform:uppercase;color:#777}
.main-nav a{color:inherit;text-decoration:none}
.main-nav .sep{margin:0 12px;color:#aaa}
.main-nav .current{color:var(--teal-text)}

.hero{left:0;top:113px;width:934px;height:393px;background:var(--teal)}
.hero-art{left:146px;top:132px;width:264px;height:244px;border-radius:50%;background:radial-gradient(circle,#e6e9ea 0%,#9ab8bd 55%,#3a6d78 100%)}
.dots{left:255px;top:404px;display:flex;gap:5px}
.dots span{width:11px;height:11px;border-radius:50%;background:var(--white)}
.dots span.active{background:transparent;border:2px solid var(--white)}
.hero-title{left:457px;top:186px;font-family:"Open Sans",sans-serif;font-weight:400;font-size:19.5px;color:var(--white);text-transform:uppercase;white-space:nowrap}
.hero-text{left:458px;top:223px;width:317px;font-family:"Open Sans",sans-serif;font-size:10.3px;line-height:13.4px;color:var(--white);text-align:justify}
.btn-read{left:458px;top:330px;width:89px;height:29px;background:var(--teal-dark);color:var(--white);font-size:10.5px;display:flex;align-items:center;justify-content:center}

.service-card{top:441px;width:207px;height:98px;background:var(--card);color:var(--white);padding:13px 10px 13px 18px}
.service-card h3{font-weight:400;font-size:9px;text-transform:uppercase;margin-bottom:8px;white-space:nowrap}
.service-card p{font-size:8.6px;line-height:13.4px;color:#dbe6ec;width:168px}
.service-card .more{position:absolute;right:0;bottom:0;width:50px;height:17px;background:var(--teal);font-size:8.8px;display:flex;align-items:center;justify-content:center}

.section-title{display:flex;align-items:center;gap:7px;font-family:"Open Sans",sans-serif;font-weight:600;font-size:13.5px;color:var(--teal-text);text-transform:uppercase}
.section-title i{width:18px;height:18px;border-radius:50%;background:var(--teal)}
.welcome-photo{left:146px;top:596px;width:163px;height:112px;background:linear-gradient(135deg,#d9dcdf,#8d9399 60%,#3d4248)}
.welcome-text{font-size:9px;line-height:13.4px;color:#8a8a8a;text-align:justify}
.link-more{color:var(--orange);font-size:8.8px}

.services-list{left:576px;top:589px;list-style:none;font-size:8.8px;color:#8a8a8a}
.services-list li{height:20px;display:flex;align-items:center;gap:8px}
.services-list li::before{content:"";width:4px;height:4px;border-radius:50%;background:var(--teal)}
.services-list li:first-child::before{background:var(--orange)}

.blog{left:146px;top:775px;width:641px;height:310px;border:1px solid var(--line);border-radius:3px;background:#fbfbfb}
.blog-arrows{right:30px;top:20px;display:flex;gap:2px}
.blog-arrows span{width:14px;height:13px;display:flex;align-items:center;justify-content:center}
.post{left:16px;width:600px}
.post h4{font-weight:400;font-size:9.6px;color:var(--teal-text)}
.post p{font-size:8.8px;line-height:13.4px;color:#8a8a8a;margin-top:12px}
.post p a{color:var(--teal-text);text-decoration:none}
.post-meta{position:absolute;right:0;top:0;display:flex;gap:20px;font-size:9.6px;color:var(--teal-text)}
.post-meta span{display:flex;align-items:center;gap:4px}
.badge{width:12px;height:12px;border-radius:50%;background:var(--teal);color:var(--white);font-size:7px;display:flex;align-items:center;justify-content:center}
.rule{left:20px;width:600px;border-top:1px dashed #cfcfcf}

.footer-nav{left:0;top:1108px;width:934px;height:38px;background:var(--teal);display:flex;justify-content:center;align-items:center;font-size:9.6px;color:var(--white)}
.footer-nav .sep{margin:0 11px}
.footer-bottom{left:0;top:1146px;width:934px;height:54px;background:var(--navy)}
.copyright{left:146px;top:1167px;font-size:8.8px;color:#dbe3e8}
.footer-brand{left:680px;top:1161px;display:flex;align-items:center;gap:5px}
.footer-brand .brand-dot{width:20px;height:20px}
.footer-brand .brand-name{font-size:15px}
</style>
</head>
<body>

<header class="site-header abs">
  <div class="brand abs"><span class="brand-dot"></span><span class="brand-name">Vantrel Media</span></div>
  <div class="social abs" aria-label="Social links"><span></span><span></span><span></span></div>
  <div class="search abs">Search
    <svg width="13" height="13" viewBox="0 0 13 13"><circle cx="5.5" cy="5.5" r="4" fill="none" stroke="#dfe8ee" stroke-width="1.4"/><line x1="8.5" y1="8.5" x2="12" y2="12" stroke="#dfe8ee" stroke-width="1.6"/></svg>
  </div>
</header>

<nav class="main-nav abs">
  <a class="current">Software Training and Implementation</a><span class="sep">|</span>
  <a>Project Management</a><span class="sep">|</span>
  <a>Business Process Analysis</a><span class="sep">|</span>
  <a>Blog</a><span class="sep">|</span>
  <a>About Us</a><span class="sep">|</span>
  <a>Contact</a>
</nav>

<section class="hero abs"></section>
<div class="hero-art abs" role="img" aria-label="Photo collage of business people meeting and shaking hands, set in rounded shapes"></div>
<div class="dots abs"><span class="active"></span><span></span><span></span></div>
<h1 class="hero-title abs">Specialist Business Consultants</h1>
<p class="hero-text abs">Cloud computing spending is due to account for a third of annual IT expenditure growth by the end of 2013. Every year the range of cloud software systems gets bigger, now including Plumora Accounting, Cloudora Apps for Business, Fieldcraft Job Management Software, Northway Deskline, Crewlink Project Manager and many more. Signing up for cloud software is only the first part of the process, and then it has to be implemented into your business.</p>
<div class="btn-read abs">READ MORE</div>

<article class="service-card abs" style="left:146px">
  <h3>Plumora Training and Implementation</h3>
  <p>Vantrel Media are experts in every aspect of a migration into Plumora for accounting, whether you are a new business or</p>
  <span class="more">MORE</span>
</article>
<article class="service-card abs" style="left:364px">
  <h3>Jobtrail Training &amp; Implementation</h3>
  <p>With a background in software implementation for trade businesses, Vantrel Media are able to guide you through</p>
  <span class="more">MORE</span>
</article>
<article class="service-card abs" style="left:580px">
  <h3>Software Training &amp; Implementation</h3>
  <p>Vantrel Media are experts in every aspect of a migration into Plumora for accounting, whether you are a new business or</p>
  <span class="more">MORE</span>
</article>

<h2 class="section-title abs" style="left:146px;top:566px"><i></i>Welcome to Vantrel Media</h2>
<div class="welcome-photo abs" role="img" aria-label="Photo of a business team working together at a laptop"></div>
<p class="welcome-text abs" style="left:320px;top:594px;width:232px">Cloud computing spending is due to account for a third of annual IT expenditure growth by the end of 2013. Every year the range of cloud software systems gets bigger, now including Plumora Accounting, Cloudora Apps for Business, Fieldcraft Job Management Software, Northway Deskline, Crewlink Project Manager and many more. Signing up for cloud software is only the first part of the process, and then it has to be implemented into your business. That's where Vantrel Media comes in.</p>
<p class="welcome-text abs" style="left:146px;top:713px;width:406px;text-align:left">Formed in 2011, and with a history in cloud computing, implementation and support, we know there's much more to software implementation and effective business use than the purchase.</p>
<span class="link-more abs" style="left:529px;top:737px">MORE</span>

<h2 class="section-title abs" style="left:576px;top:566px"><i></i>Our Services</h2>
<ul class="services-list abs">
  <li>Lorem Ipsum is simply dummy</li>
  <li>Text of the printing and typesetting</li>
  <li>Industry. Lorem Ipsum has been</li>
  <li>Industry's standard dummy text ever since</li>
  <li>when an unknown printer took a galley</li>
  <li>Type only five centuri</li>
  <li>Lorem Ipsum is simply dummy</li>
  <li>Text of the printing and typesetting</li>
</ul>

<section class="blog abs">
  <h2 class="section-title abs" style="left:16px;top:16px"><i></i>Blog Post</h2>
  <div class="blog-arrows abs">
    <span style="background:var(--teal)"><svg width="8" height="5"><polyline points="1,4.5 4,1.5 7,4.5" fill="none" stroke="#fff" stroke-width="1.2"/></svg></span>
    <span style="background:var(--navy)"><svg width="8" height="5"><polyline points="1,0.5 4,3.5 7,0.5" fill="none" stroke="#fff" stroke-width="1.2"/></svg></span>
  </div>

  <div class="post abs" style="top:48px">
    <h4>Inboxa Mail to Cloudora Apps</h4>
    <div class="post-meta"><span><b class="badge">8</b>Comment</span><span><b class="badge">›</b>Submit a Comment</span></div>
    <p>With Northway making big strides recently to move their huge office suite into the cloud, with Northway Deskline, this is a great time to revisit the options with Cloudora Apps providing a great alternative for small businesses to avoid the large costs and resources required to manage a full Northway Mailhub operation. <a>[More]</a></p>
  </div>
  <div class="rule abs" style="top:126px"></div>

  <div class="post abs" style="top:139px">
    <h4>So why Cloud Software...?</h4>
    <div class="post-meta"><span><b class="badge">6</b>Comment</span><span><b class="badge">›</b>Submit a Comment</span></div>
    <p>Cloud software is a massive area of the market and has emerged as a viable choice for many areas of business in the last year or two. There are however still a lot of misunderstandings and urban myths lurking out there, so we will use this post to hopefully provide some clear information. <a>[More]</a></p>
  </div>
  <div class="rule abs" style="top:208px"></div>

  <div class="post abs" style="top:222px">
    <h4>TalkHall, Learnly, Brightwell Academy and the shift in education</h4>
    <div class="post-meta"><span><b class="badge">9</b>Comment</span><span><b class="badge">›</b>Submit a Comment</span></div>
    <p>In a traditional sense, a person's knowledge and education tends to be defined by the school they went to, the college they graduated from and the degree subject and mark that they received. In recent years however there has been a huge shift into online education, and some fantastic new technologies which are helping to enable this. <a>[More]</a></p>
  </div>
</section>

<nav class="footer-nav abs">
  <span>Home</span><span class="sep">|</span>
  <span>Software Training and Implementation</span><span class="sep">|</span>
  <span>Blog</span><span class="sep">|</span>
  <span>About Us</span><span class="sep">|</span>
  <span>Project Management</span><span class="sep">|</span>
  <span>Business Process Analysis</span><span class="sep">|</span>
  <span>Contact us</span>
</nav>
<footer class="footer-bottom abs"></footer>
<p class="copyright abs">Copyright © 2013 Vantrel Media All right reserved.&nbsp; Powered by</p>
<div class="footer-brand abs"><span class="brand-dot"></span><span class="brand-name">Vantrel Media</span></div>

</body>
</html>
```